Web Design Business Card

I need a new business card designed, we recently rebranded and I need to get a fresh design to match our new logo, colours and branding.

Details:

Dorin Vaskel | Founder & CEO
Address: 7 Fernbrook Lane, #14-05 Maralune Crest, Singapore 318457
Tel: +65 93640281
Web: www.plumtrove.com.sg
hello@plumtrove.com.sg

I've attached my old card as well

Industry/Entity Type

Business

Requirements
Must have
• Front and Back
Interesting use of logo
Correct use of colour scheme

```html
<!DOCTYPE html>
<html lang="en">
<head>
<meta charset="utf-8">
<title>Plumtrove Business Card – Front and Back</title>
<link rel="stylesheet" href="https://fonts.googleapis.com/css2?family=Open+Sans:wght@400;700&display=swap">
<style>
  :root {
    --stage: #6d6d6f;
    --card-white: #ffffff;
    --card-silver: #c9cacc;
    --card-silver-light: #f2f2f3;
    --brand-blue: #3fb8ec;
    --brand-blue-light: #8ad7f6;
    --brand-brown: #7a6d68;
    --text-grey: #5f5f62;
  }
  * { margin: 0; padding: 0; box-sizing: border-box; }
  html, body { width: 1200px; height: 400px; overflow: hidden; }
  body {
    background: var(--stage);
    font-family: "Open Sans", Arial, sans-serif;
    position: relative;
  }
  .card {
    position: absolute;
    overflow: hidden;
  }
  .card-front {
    left: 58px; top: 62px; width: 522px; height: 277px;
    background: radial-gradient(ellipse 60% 60% at 50% 50%, var(--card-white) 0%, var(--card-silver-light) 45%, var(--card-silver) 100%);
  }
  .card-back {
    left: 616px; top: 61px; width: 523px; height: 277px;
    background: var(--card-white);
  }
  .brand {
    position: absolute;
    display: flex;
    align-items: center;
  }
  .brand-dot {
    border-radius: 50%;
    background: linear-gradient(180deg, var(--brand-blue) 0%, var(--brand-blue-light) 100%);
    flex: none;
  }
  .brand-name {
    color: var(--brand-brown);
    font-weight: 700;
    letter-spacing: -0.5px;
    line-height: 1;
  }
  .card-front .brand { left: 117px; top: 98px; }
  .card-front .brand-dot { width: 78px; height: 78px; margin-right: 18px; }
  .card-front .brand-name { font-size: 50px; }
  .back-header {
    position: absolute; left: 0; top: 0; width: 100%; height: 94px;
    background: radial-gradient(ellipse 45% 90% at 50% 40%, var(--card-white) 0%, var(--card-silver-light) 40%, var(--card-silver) 100%);
  }
  .card-back .brand { left: 155px; top: 15px; }
  .card-back .brand-dot { width: 59px; height: 59px; margin-right: 12px; }
  .card-back .brand-name { font-size: 35px; }
  .glow-line {
    position: absolute; height: 4px;
    background: linear-gradient(90deg, transparent 0%, var(--brand-blue-light) 10%, var(--brand-blue) 50%, var(--brand-blue-light) 90%, transparent 100%);
  }
  .glow-line.header-edge { left: 131px; top: 92px; width: 241px; }
  .glow-line.footer-edge { left: 141px; top: 272px; width: 240px; height: 3px; }
  .divider {
    position: absolute; left: 184px; top: 169px; width: 166px; height: 1px;
    background: linear-gradient(90deg, transparent, var(--brand-blue) 30%, var(--brand-blue) 70%, transparent);
  }
  .contact {
    position: absolute; left: 0; width: 100%;
    text-align: center; color: var(--text-grey); white-space: nowrap;
  }
  .person-name { top: 117px; font-size: 18px; color: var(--brand-blue); }
  .person-role { top: 140px; font-size: 13px; }
  .address { top: 182px; font-size: 14px; }
  .phone { top: 206px; font-size: 14px; }
  .online { top: 234px; font-size: 14px; }
  .online span + span { margin-left: 18px; }
</style>
</head>
<body>
  <section class="card card-front" aria-label="Card front">
    <div class="brand">
      <span class="brand-dot"></span>
      <span class="brand-name">plumtrove</span>
    </div>
  </section>

  <section class="card card-back" aria-label="Card back">
    <div class="back-header"></div>
    <div class="brand">
      <span class="brand-dot"></span>
      <span class="brand-name">plumtrove</span>
    </div>
    <div class="glow-line header-edge"></div>
    <p class="contact person-name">Dorin Vaskel</p>
    <p class="contact person-role">Founder &amp; CEO</p>
    <div class="divider"></div>
    <p class="contact address">7 Fernbrook Lane, #14-05 Maralune Crest, Singapore 318457</p>
    <p class="contact phone">+65 93640281</p>
    <p class="contact online"><span>hello@plumtrove.com.sg</span><span>www.plumtrove.com.sg</span></p>
    <div class="glow-line footer-edge"></div>
  </section>
</body>
</html>
```